Escape Room Brochure, Trifold. Bold Black, yellow red. Doors Keys

We need a brochure to introduce our escape room and our services.
Attached are some of our designs as well as some examples of brochures we like.
We are THE VAULTS of KMD, however, we are aiming at Can you outwit the vaults of KMD.
We are one of three escape rooms in a college town. We believe our rooms are more creative and original. Only family friendly. Brochure to be distributed to explain what an escape room is and promote our new fundraising program.

Font styles to use
Other font styles liked:
• impact

Colors
fbee3e
ec1f27
000000
dbdbdb

Requirements
Must have
• description of our rooms. services we offer. Fundraising and group teambuilding. Most information can be found at thevaultsofkmd.example
• what is an escape room.
Nice to have
• Photoshop
Should not have
• padlock or maze

```html
<!DOCTYPE html>
<html lang="en">
<head>
<meta charset="utf-8">
<title>THE VAULTS of KMD – Trifold Brochure</title>
<link rel="stylesheet" href="https://fonts.googleapis.com/css2?family=Anton&family=Questrial&display=swap">
<style>
  :root{
    --yellow:#fbee3e;
    --red:#ec1f27;
    --black:#000;
    --grey:#dbdbdb;
    --stage:#97989c;
    --body-grey:#4a4a4a;
    --body-font:'Questrial', Arial, sans-serif;
    --display-font:'Anton', Impact, sans-serif;
  }
  *{box-sizing:border-box;margin:0;padding:0}
  html,body{width:1138px;height:1200px;overflow:hidden}
  body{background:var(--stage);font-family:var(--body-font);position:relative}

  .spread{position:absolute;left:190px;width:795px;height:615px;transform:scale(.956);transform-origin:0 0;display:flex;box-shadow:0 4px 14px rgba(0,0,0,.35)}
  .spread--outside{top:30px}
  .spread--inside{top:628px}

  .panel{position:relative;width:265px;height:615px;overflow:hidden}
  .panel--white{background:#fff;color:var(--body-grey)}
  .panel--black{background:var(--black);color:#fff}
  .panel--light{background:linear-gradient(90deg,#f4f4f4,#e6e6e6);color:var(--body-grey)}
  .panel--grey{background:linear-gradient(90deg,#d7d7d7,#ececec);color:var(--body-grey)}

  .abs{position:absolute}
  .stripes{position:absolute;left:0;width:265px}
  .photo{position:absolute;border:0}
  .body-text{font-size:9.2px;line-height:1.33}
  .small-text{font-size:7.6px;line-height:1.3}
  .fine-text{font-size:7.2px;line-height:1.3}

  .wordmark{position:absolute;font-family:var(--body-font);color:#fff;text-align:center;letter-spacing:1px;line-height:1}
  .wordmark span{display:block}
  .wordmark__main{font-size:22px;letter-spacing:3px}
  .wordmark__sub{font-size:11px;text-align:right;letter-spacing:2px;margin-top:2px}

  .tab{position:absolute;height:24px;background:var(--red);color:var(--yellow);font-size:14px;line-height:24px;padding-left:12px;clip-path:polygon(0 0,86% 0,100% 100%,0 100%)}

  /* outside panel 1 */
  .welcome{left:18px;top:160px;font-size:15px;color:#111;white-space:nowrap}
  .welcome b{font-weight:normal;letter-spacing:1px}
  .intro{left:18px;top:190px;width:228px}
  .callout{left:20px;top:322px;width:225px;height:92px;background:var(--yellow);border-radius:8px;color:#222;text-align:center;padding:10px 10px 0;font-size:9px;line-height:1.32}
  .outro{left:18px;top:428px;width:230px}
  .footer-band{left:0;top:560px;width:265px;height:55px;background:var(--black);color:#fff;font-size:11.5px;padding:24px 0 0 22px}

  /* outside panel 2 */
  .hours{left:28px;top:94px;width:210px;text-align:center;font-size:10.4px;line-height:1.27}
  .hours .lead{color:var(--yellow)}
  .hours .phone{color:var(--yellow)}
  .contact-title{left:0;width:265px;top:424px;text-align:center;color:var(--red);font-size:17px}
  .contact-address{left:0;width:265px;top:456px;text-align:center;font-size:11.5px;line-height:1.35}
  .contact-phone{left:0;width:265px;top:500px;text-align:center;color:var(--yellow);font-size:21px}
  .contact-mail{left:0;width:265px;top:540px;text-align:center;font-size:11px}

  /* cover */
  .cover-tag{left:27px;top:75px;width:234px;height:35px;background:var(--red);color:var(--yellow);font-size:13.5px;line-height:35px;padding-left:10px;white-space:nowrap;clip-path:polygon(0 0,90% 0,100% 100%,0 100%)}
  .door{left:30px;top:230px;width:235px;height:385px;background:radial-gradient(ellipse at 18% 40%,rgba(255,255,255,.95) 0,rgba(255,255,255,.35) 12%,rgba(120,120,120,.25) 38%,rgba(0,0,0,0) 70%)}
  .headline{right:28px;top:455px;text-align:right;font-family:var(--display-font);font-size:33px;line-height:1;letter-spacing:.5px}
  .headline .y{color:var(--yellow)} .headline .r{color:var(--red)}
  .cover-rule{left:105px;top:567px;width:135px;height:1px;background:var(--yellow)}
  .cover-url{right:24px;top:578px;font-size:11px}

  /* inside panel 1 */
  .header-band{left:0;top:0;width:265px;height:58px;background:var(--black);color:var(--yellow);font-size:17px;padding:16px 0 0 23px}
  .what{left:24px;top:85px;width:218px}
  .services{left:22px;top:220px;font-size:19px;color:#111}
  .parties-text{left:20px;top:402px;width:228px}

  /* inside panel 3 */
  .games-title{left:25px;top:16px;font-size:20px;color:var(--yellow)}
  .game{position:absolute;left:28px;width:215px;display:flex;gap:8px;align-items:flex-start}
  .game .dot{flex:0 0 60px;height:60px;border-radius:50%}
  .game p{font-size:8.4px;line-height:1.32;color:#fff}
  .game b{color:var(--yellow)}
  .announce{left:28px;top:233px;font-size:14px;line-height:1.25}
  .opening{left:96px;top:288px;font-size:16.5px;line-height:1.28;color:var(--yellow)}
  .opening-dot{left:28px;top:291px;width:60px;height:60px;border-radius:50%;background:radial-gradient(circle,#8a8377,#3a352f 70%,#1b1814)}
  .closing{left:24px;width:225px;font-size:11px;line-height:1.3}
  .closing--horror{top:366px}
  .closing--family{top:404px}
  .closing--fundraising{top:442px;color:var(--yellow)}
</style>
</head>
<body>

<!-- OUTSIDE SPREAD -->
<section class="spread spread--outside">

  <div class="panel panel--white">
    <div class="photo" style="left:0;top:0;width:265px;height:130px;background:linear-gradient(135deg,#2a2a2a,#9a9a9a 50%,#303030)" role="img" aria-label="Black and white pile of antique keys"></div>
    <svg class="stripes" style="top:118px" height="30" viewBox="0 0 265 30"><polygon points="0,12 265,0 265,10 0,22" fill="#fbee3e"/><polygon points="0,22 265,10 265,16 0,28" fill="#ec1f27"/></svg>
    <p class="abs welcome">Welcome to <b>THE VAULTS of KMD</b></p>
    <p class="abs body-text intro">We are a Millbrook Texas based escape game experience with three rooms currently available and a fourth room on the way! We offer richly thematic escape rooms with great puzzles and mysteries relevant to each room. Our escape games are a great way to spend a weekend with 2 to 10 friends. Each escape room lasts about an hour, with varying difficulties and experiences.</p>
    <div class="abs callout">Our newest escape room, <b>'The Cellar of Shadows'</b> offers a heart-pounding and thrilling experience. Our goal is to provide an fun-filled hour that will keep groups tense and excited up until the final seconds.</div>
    <p class="abs body-text outro">We have something for any group here at The Vaults of KMD! Book online today, or contact us by phone. We are a local family-business, which makes us very prepared to work with you and your group to ensure you get the best experience possible. If you have any questions, especially if you want to book a party or special event at our business, call us at <b style="color:#111">(555) 014-7299!</b></p>
    <svg class="stripes" style="top:538px" height="24" viewBox="0 0 265 24"><polygon points="75,12 265,0 265,7 75,19" fill="#fbee3e"/><polygon points="0,22 265,6 265,14 0,24" fill="#ec1f27"/></svg>
    <div class="abs footer-band">We look forward to hearing from you!</div>
  </div>

  <div class="panel panel--black">
    <div class="abs hours">
      <span class="lead">Our current business hours are:</span><br>
      Monday through Thursday from 4:00 pm - 10:30 pm<br>
      Fridays from 3:00 pm - 11:30 pm and Saturdays from 1:00 pm 11:30 pm<br>
      We are closed on Sundays, but if you would like to book u can contact us by phone at<br>
      <span class="phone">(555)-014-7210</span> or by email at info@thevaultsofkmd.example, and we will do what we can to accomodate you.
    </div>
    <div class="wordmark" style="left:52px;top:368px"><span class="wordmark__main">THE VAULTS</span><span class="wordmark__sub">of KMD</span></div>
    <p class="abs contact-title">Contact Us</p>
    <p class="abs contact-address">4120 Harbor Lane Suite 12,<br>Millbrook TX</p>
    <p class="abs contact-phone">(555) 014-7210</p>
    <p class="abs contact-mail">info@thevaultsofkmd.example</p>
  </div>

  <div class="panel panel--black">
    <div class="abs door" role="img" aria-label="Dark door opening with bright light spilling across the floor"></div>
    <div class="abs cover-tag">Can you outwit the Vaults of KMD?</div>
    <div class="wordmark" style="left:30px;top:125px"><span class="wordmark__main" style="font-size:26px">THE VAULTS</span><span class="wordmark__sub" style="font-size:13px">of KMD</span></div>
    <div class="abs headline"><span class="y">LIVE</span><br><span class="r">ESCAPE</span><br><span class="y">GAMES</span></div>
    <div class="abs cover-rule"></div>
    <p class="abs cover-url">www.thevaultsofkmd.example</p>
  </div>
</section>

<!-- INSIDE SPREAD -->
<section class="spread spread--inside">

  <div class="panel panel--light">
    <div class="abs header-band">What is an Escape Room</div>
    <svg class="stripes" style="top:52px" height="24" viewBox="0 0 265 24"><polygon points="0,6 265,0 265,8 0,14" fill="#ec1f27"/><polygon points="0,14 265,8 265,12 0,20" fill="#fbee3e"/></svg>
    <p class="abs body-text what">The Vaults of KMD is a <b style="color:#111">"real life"</b> escape game in which teams of 2-10 are locked in a deeply thematic room and given 1 hour to find their way out. By searching for clues, solving puzzles, and discovering the secrets each of our rooms have to offer, teams will attempt to beat the clock in this creative new form of entertainment.</p>
    <p class="abs services">Our Services</p>
    <div class="tab" style="left:20px;top:255px;width:105px">Parties</div>
    <div class="photo" style="left:20px;top:280px;width:236px;height:112px;background:linear-gradient(120deg,#6b4a35,#c9a27a 45%,#5d3b2a)" role="img" aria-label="Group of friends in party hats celebrating"></div>
    <div class="abs parties-text">
      <p class="small-text" style="color:#111;font-size:8px">At THE VAULTS of KMD we love to make your special events even more fun.</p>
      <p class="small-text" style="margin-top:8px">The Vaults of KMD is a great place to have your next party or special event. We have a great area near the back of our business where you and your group can relax and have a nice celebration after your time in one or more of our escape rooms. We can comfortably fit up to 25 people for your party, and we can run multiple escape games at once. We would be happy to help you plan your party if you call us at (555)-014-7210 or e-mail us at info@thevaultsofkmd.example.</p>
    </div>
    <svg class="stripes" style="top:578px" height="24" viewBox="0 0 265 24"><polygon points="0,8 265,0 265,7 0,15" fill="#ec1f27"/><polygon points="0,15 200,9 200,14 0,20" fill="#fbee3e"/></svg>
  </div>

  <div class="panel panel--grey">
    <div class="tab" style="left:15px;top:16px;width:120px">Date Night</div>
    <div class="photo" style="left:15px;top:40px;width:236px;height:102px;background:linear-gradient(110deg,#c9a071,#f1d7b6 50%,#8d6b4d)" role="img" aria-label="Smiling couple on a date night"></div>
    <div class="abs" style="left:15px;top:148px;width:238px">
      <p class="small-text" style="color:#111;font-size:8.2px">THE VAULTS Escape Games are the perfect place to enjoy a unique, one-of-a-kind experience together!</p>
      <p class="small-text" style="color:#111;font-size:8.2px;margin-top:9px">THE PERFECT CHALLENGE FOR</p>
      <p class="fine-text" style="margin-top:8px"><b>The First Date:</b> A great way to break the ice and challenge yourself you interact with each other! Nothing says "You're the coolest person I know!" more than taking your new girlfriend on a date to the THE VAULTS Escape Games!</p>
      <p class="fine-text" style="margin-top:8px"><b>The Third Date:</b> Show her you're committed by locking yourself in a room with her for 60 minutes and working together to find a way out!</p>
      <p class="fine-text" style="margin-top:8px"><b>Anniversary:</b> Want a memorable experience that she isn't soon to forget? An experience that will have her talking to her friends and family about how great of a guy you really are?</p>
    </div>
    <div class="tab" style="left:15px;top:335px;width:135px">Team Building</div>
    <div class="photo" style="left:15px;top:359px;width:236px;height:85px;background:linear-gradient(100deg,#3b2d22,#7a634c 50%,#2e241b)" role="img" aria-label="Hands placing puzzle pieces around an open notebook on a wooden table"></div>
    <p class="abs small-text" style="left:15px;top:454px;width:238px">Escape games are well-known for being great for team-building. The escape room experience forces everyone in the room to work together, share information, and discuss problems in order to escape in time. They are an amazing option for co-workers looking to boost morale, promote teamwork, or just to create a nice ice-breaker situation that everyone will remember.</p>
  </div>

  <div class="panel panel--black">
    <p class="abs games-title">Our Games</p>
    <div class="game" style="top:62px">
      <div class="dot" style="background:radial-gradient(circle,#e0c23a,#c2361f 45%,#2a4f8f 80%)" role="img" aria-label="Colourful nineties themed collage"></div>
      <p>Our <b>'Rewind the 90's'</b> escape game is fun for all ages. Families and groups of 90's kids have been enjoying this room since March 2016.</p>
    </div>
    <div class="game" style="top:145px">
      <div class="dot" style="background:radial-gradient(circle,#8fa6d6,#3c4c86 55%,#0e1430)" role="img" aria-label="Gloved hand against a glass pane"></div>
      <p><b>'The Silent Outbreak'</b> escape room has been open since July 2016, and groups have been enjoying the extra challenge and complex medical/science themed clues.</p>
    </div>
    <p class="abs announce">We are also proud to<br>announce that</p>
    <div class="abs opening-dot" role="img" aria-label="Dim, eerie cellar room"></div>
    <p class="abs opening">The Cellar<br>of Shadows<br>is NOW OPEN.</p>
    <p class="abs closing closing--horror">Customers have been enjoying the scary, horror-movie style atmosphere!</p>
    <p class="abs closing closing--family">THE VAULTS of KMD is a family business. We are proud to offer something for everyone.</p>
    <p class="abs closing closing--fundraising">Ask about our new fundraising program for schools, clubs and teams!</p>
    <div class="wordmark" style="left:55px;top:492px"><span class="wordmark__main">THE VAULTS</span><span class="wordmark__sub">of KMD</span></div>
    <svg class="stripes" style="top:548px" height="28" viewBox="0 0 265 28"><polygon points="60,10 265,2 265,10 60,18" fill="#fbee3e"/><polygon points="0,20 265,10 265,16 0,26" fill="#ec1f27"/></svg>
    <p class="abs cover-url" style="top:581px">www.thevaultsofkmd.example</p>
  </div>
</section>

</body>
</html>
```